Needing a business Card for new fire company.

Dulvan, sales fire equipment and parts. We also do tree clearing for the forest service. My logo will be attached to this. I am also looking for a design that when people see the card it stick with them and they will remember my sales team giving it to them.

```html
<!DOCTYPE html>
<html lang="en">
<head>
<meta charset="utf-8">
<title>Dulvan Business Card</title>
<link href="https://fonts.googleapis.com/css2?family=Arimo:wght@400;700&display=swap" rel="stylesheet">
<style>
  :root {
    --page: #262626;
    --card-dark: #1f1f1f;
    --card-light: #ffffff;
    --ember-red: #c1272d;
    --ink: #1e1e1e;
    --text-light: #f2f2f2;
  }
  * { box-sizing: border-box; margin: 0; padding: 0; }
  html, body {
    width: 1200px; height: 988px; overflow: hidden;
    background: var(--page);
    font-family: "Arimo", Arial, sans-serif;
  }
  .card {
    position: absolute;
    width: 560px; height: 320px;
    border-radius: 22px;
    overflow: hidden;
    box-shadow: 0 10px 30px rgba(0,0,0,0.45);
  }
  .card-front {
    left: 50px; top: 110px;
    background: var(--card-dark);
    display: flex; align-items: center; justify-content: center;
  }
  .card-back {
    left: 590px; top: 548px;
    background: var(--card-light);
  }
  .brand { display: flex; align-items: center; gap: 14px; }
  .brand-mark {
    width: 22px; height: 22px; border-radius: 50%;
    background: var(--ember-red);
  }
  .brand-name {
    font-weight: 700; font-size: 72px; letter-spacing: 2px;
    text-transform: uppercase; line-height: 1;
  }
  .card-front .brand-name { color: var(--text-light); }
  .card-back .brand { position: absolute; left: 40px; top: 100px; }
  .card-back .brand-name { color: var(--ink); font-size: 50px; }
  .card-back .brand-mark { width: 18px; height: 18px; }
  .wave { position: absolute; inset: 0; width: 100%; height: 100%; }
  .contact {
    position: absolute; right: 24px; top: 118px;
    text-align: right; color: var(--text-light);
    font-size: 12.5px; line-height: 1.35;
  }
  .contact-name {
    color: var(--ember-red); font-weight: 700; font-size: 20px;
    text-transform: uppercase; letter-spacing: 0.5px; line-height: 1.05;
  }
  .contact-role { font-size: 14px; margin-bottom: 8px; }
  .contact-address { margin-bottom: 10px; }
  .contact-line { display: flex; justify-content: flex-end; align-items: center; gap: 6px; }
  .contact-icon { width: 11px; height: 11px; flex: none; }
  .contact-icon path, .contact-icon circle, .contact-icon rect { fill: var(--ember-red); }
  .spacer { width: 11px; flex: none; }
</style>
</head>
<body>
  <section class="card card-front">
    <div class="brand">
      <span class="brand-mark"></span>
      <span class="brand-name">Dulvan</span>
    </div>
  </section>

  <section class="card card-back">
    <svg class="wave" viewBox="0 0 560 320" preserveAspectRatio="none" aria-hidden="true">
      <path d="M0,226 C150,290 265,270 294,176 C318,88 390,46 560,34 L560,320 L0,320 Z" fill="var(--ember-red)"/>
      <path d="M0,242 C155,302 272,282 302,184 C327,96 395,56 560,44 L560,320 L0,320 Z" fill="var(--card-light)"/>
      <path d="M0,254 C160,312 280,290 310,190 C335,100 400,60 560,48 L560,320 L0,320 Z" fill="var(--card-dark)"/>
      <path d="M150,302 C250,292 300,252 326,200 C312,252 252,292 150,302 Z" fill="var(--card-light)"/>
    </svg>

    <div class="brand">
      <span class="brand-mark"></span>
      <span class="brand-name">Dulvan</span>
    </div>

    <div class="contact">
      <div class="contact-name">Reid Halvorsen</div>
      <div class="contact-role">CEO/Founder</div>
      <div class="contact-address">
        <div class="contact-line">P.O. Box 48 Tarrow AB<span class="spacer"></span></div>
        <div class="contact-line">Country Name 3107<span class="spacer"></span></div>
      </div>
      <div class="contact-line">02 5550 0417
        <svg class="contact-icon" viewBox="0 0 12 12"><path d="M2.5 1 L4.5 1 L5.2 3.6 L4 4.6 C4.7 6 6 7.3 7.4 8 L8.4 6.8 L11 7.5 L11 9.5 C11 10.3 10.3 11 9.5 11 C5 11 1 7 1 2.5 C1 1.7 1.7 1 2.5 1 Z"/></svg>
      </div>
      <div class="contact-line">info@emberlinestudio.com
        <svg class="contact-icon" viewBox="0 0 12 12"><rect x="0.5" y="2" width="11" height="8" rx="1"/></svg>
      </div>
      <div class="contact-line">www.emberlinestudio.com
        <svg class="contact-icon" viewBox="0 0 12 12"><circle cx="6" cy="6" r="5.5"/></svg>
      </div>
    </div>
  </section>
</body>
</html>
```